Cybersecurity firm needs marketing template for professional services

Looking for a flyer design we can use as a template to market ten professional cybersecurity services (Pen Testing, V-CISO, SOC 2, KORVALD, etc). Each flyer will explain WHAT the service is, WHO needs it, DIFFERENT TYPES and SCOPE. Clean look/ lots of white space/ elevated graphics, Attached is a basic example but we are looking for something to WOW us.

```html
<!DOCTYPE html>
<html lang="en">
<head>
<meta charset="utf-8">
<title>Penetration Testing – Service Flyer</title>
<link href="https://fonts.googleapis.com/css2?family=Montserrat:wght@500;600;700&family=Nunito+Sans:wght@300;400&display=swap" rel="stylesheet">
<style>
  :root {
    --stage: #9a9a9a;
    --paper: #ffffff;
    --brand-blue: #0a84c6;
    --accent-blue: #2ea3dc;
    --band-grey: #bdbec0;
    --text-grey: #8a8a8a;
    --name-grey: #7a7a7a;
  }
  * { margin: 0; padding: 0; box-sizing: border-box; }
  html, body { width: 1200px; height: 1200px; overflow: hidden; background: var(--stage); }
  .flyer {
    position: absolute; left: 172px; top: 0;
    width: 856px; height: 1200px;
    background: var(--paper);
    font-family: "Nunito Sans", Arial, sans-serif;
    color: var(--text-grey);
  }
  .hero { position: absolute; left: 0; top: 0; width: 856px; height: 377px; }
  .hero svg { display: block; width: 100%; height: 100%; }

  .brand { position: absolute; left: 40px; top: 100px; }
  .brand-name {
    display: flex; align-items: center; gap: 10px;
    font-family: "Nunito Sans", Arial, sans-serif;
    font-weight: 400; font-size: 27px; line-height: 32px; color: var(--name-grey);
  }
  .brand-square { width: 18px; height: 18px; background: var(--accent-blue); }
  .brand-tagline {
    margin-top: 6px; font-size: 13px; color: var(--name-grey);
    letter-spacing: 1.2px; text-transform: uppercase;
  }

  .hero-title {
    position: absolute; left: 39px; top: 193px;
    font-family: "Montserrat", Arial, sans-serif; font-weight: 700;
    font-size: 43px; line-height: 44px; color: #fff;
  }
  .hero-series {
    position: absolute; left: 39px; top: 313px;
    font-family: "Montserrat", Arial, sans-serif; font-weight: 500;
    font-size: 23px; line-height: 29px; color: #fff;
  }

  .section { position: absolute; left: 39px; width: 778px; }
  .section-heading {
    display: flex; align-items: center; gap: 18px;
    font-family: "Montserrat", Arial, sans-serif; font-weight: 600;
    font-size: 27px; line-height: 34px; color: var(--accent-blue);
  }
  .section-heading::before {
    content: ""; width: 10px; height: 27px; background: var(--accent-blue);
  }
  .section-body {
    margin: 10px 0 0 28px;
    font-size: 17px; line-height: 22.5px; text-align: justify;
    text-align-last: left; font-weight: 400;
  }
  .what { top: 404px; }
  .who { top: 598px; }
  .types { top: 730px; }
  .scope { top: 882px; }

  .divider {
    position: absolute; left: 39px; top: 1049px; width: 778px; height: 2px;
    background: linear-gradient(90deg, transparent, #e2e2e2 20%, #e2e2e2 80%, transparent);
  }
  .cta {
    position: absolute; left: 0; top: 1064px; width: 856px; text-align: center;
    font-family: "Montserrat", Arial, sans-serif; font-weight: 600;
    font-size: 22px; color: var(--accent-blue);
  }
  .contact-phone {
    position: absolute; left: 39px; top: 1127px;
    display: flex; align-items: center; gap: 13px;
    font-weight: 300; font-size: 34px; color: var(--text-grey);
  }
  .icon-circle {
    width: 40px; height: 40px; border-radius: 50%; background: var(--text-grey);
    display: flex; align-items: center; justify-content: center;
  }
  .contact-list { position: absolute; left: 403px; top: 1126px; list-style: none; font-size: 14.5px; line-height: 24px; }
  .contact-list li { display: flex; align-items: center; gap: 9px; }
  .mini-icon {
    width: 15px; height: 15px; border-radius: 50%; background: var(--text-grey);
    display: flex; align-items: center; justify-content: center;
  }
</style>
</head>
<body>
<main class="flyer">
  <header class="hero">
    <svg viewBox="0 0 1180 519" preserveAspectRatio="none">
      <defs>
        <linearGradient id="skyTone" x1="0" y1="0" x2="0.6" y2="1">
          <stop offset="0" stop-color="#a9dcf6"/>
          <stop offset="0.45" stop-color="#4aa8e2"/>
          <stop offset="1" stop-color="#1f7fc4"/>
        </linearGradient>
      </defs>
      <polygon points="586,0 1180,0 1180,519 405,519 535,240" fill="url(#skyTone)" role="img" aria-label="Photo of a glass office tower seen from below against a cloudy blue sky"/>
      <polygon points="0,240 486,240 527,160 535,240 445,423 0,423" fill="#0a84c6"/>
      <polygon points="486,240 527,160 535,240" fill="#0a6ea8"/>
      <polygon points="0,423 445,423 405,519 0,519" fill="#bdbec0"/>
    </svg>
    <div class="brand">
      <div class="brand-name"><span class="brand-square"></span>Tidewell Group</div>
      <div class="brand-tagline">Security advisors</div>
    </div>
    <h1 class="hero-title">Penetration<br>Testing</h1>
    <p class="hero-series">Tidewell Insights<br>Series</p>
  </header>

  <section class="section what">
    <h2 class="section-heading">WHAT the service is</h2>
    <p class="section-body">A mature penetration test is an in-depth security assessment where ethical hackers attempt to exploit system vulnerabilities to gain access to sensitive data or systems. It is an important security practice because it can help organizations identify vulnerabilities that attackers may exploit in order to gain access to confidential information, disrupt services, or even cause physical damage to the network or system.</p>
  </section>

  <section class="section who">
    <h2 class="section-heading">WHO needs it</h2>
    <p class="section-body">A wide range of techniques are used to identify security weaknesses, such as vulnerability scanning, application security testing, manual testing, and web application testing.</p>
  </section>

  <section class="section types">
    <h2 class="section-heading">DIFFERENT TYPES</h2>
    <p class="section-body">Lorem Ipsum is simply dummy text of the printing and typesetting industry. Lorem Ipsum has been the industry's standard dummy text ever since the 1500s, when an unknown printer took a galley of type and scrambled it to make a type specimen book.</p>
  </section>

  <section class="section scope">
    <h2 class="section-heading">SCOPE</h2>
    <p class="section-body">Lorem Ipsum is simply dummy text of the printing and typesetting industry. Lorem Ipsum has been the industry's standard dummy text ever since the 1500s, when an unknown printer took a galley of type and scrambled it to make a type specimen book.</p>
  </section>

  <div class="divider"></div>
  <p class="cta">Considering a Pen Test? Contact Our Expert.</p>

  <div class="contact-phone">
    <span class="icon-circle">
      <svg width="20" height="20" viewBox="0 0 24 24"><path d="M6.6 10.8a15 15 0 0 0 6.6 6.6l2.2-2.2a1 1 0 0 1 1-.25 11 11 0 0 0 3.6.6 1 1 0 0 1 1 1V20a1 1 0 0 1-1 1A17 17 0 0 1 3 4a1 1 0 0 1 1-1h3.5a1 1 0 0 1 1 1 11 11 0 0 0 .6 3.6 1 1 0 0 1-.25 1z" fill="#fff"/></svg>
    </span>
    + 877-555-0142
  </div>

  <ul class="contact-list">
    <li>
      <span class="mini-icon"><svg width="9" height="9" viewBox="0 0 10 10"><rect x="1" y="2" width="8" height="6" fill="none" stroke="#fff" stroke-width="1"/><path d="M1 2l4 3.5L9 2" fill="none" stroke="#fff" stroke-width="1"/></svg></span>
      pentest@tidewellpro.com
    </li>
    <li>
      <span class="mini-icon"><svg width="9" height="9" viewBox="0 0 10 10"><path d="M5 9.5S2 6 2 4a3 3 0 0 1 6 0c0 2-3 5.5-3 5.5z" fill="#fff"/><circle cx="5" cy="4" r="1" fill="#8a8a8a"/></svg></span>
      2210 W. Harbor Lane, Suite 140, Ashford, IN 46019
    </li>
  </ul>
</main>
</body>
</html>
```